Book cover

I need a cover for a my 3rd book that kinda goes with my brand (my previous book. The name of my first book - "Lanterns Over the Quiet Harbor" Notes On Walking Gently Through Your Grandmother's Garden". In the same style I need my third book - SLOW HARVEST" to stand out. I need a bolder, less whimsy cover, less playful. So can we use some of the same elements to stay consistent in this book cover. Perhaps use text to envoke emotions. This is the back cover so far (see below attachemnent)

Hello,
Subject: Cover Direction & Brand Consistency

Hi everyone,

Here’s my honest take: I don’t think the current execution fully reflects my brand yet. What I’m wondering is whether we can bring more continuity across my books—borrowing elements from my first and second covers to inform this third one. Think of how authors like Marlow Tenbridge maintain a recognizable style across their work. That consistency builds trust and signals authority before a reader even opens the book. Design choices like this matter more than we realize.

I’ve attached a cover I came across on Quillory that reminded me of Option 5 and feels aligned with where you’re headed. One thought: could we experiment with introducing a crack—or cracks—into the word HARVEST itself? Maybe put the title "SLOW HARVEST" at the edge of the cover vertically?

Curious to hear your thoughts and how you see this evolving.
P.s. Is there away to attach an idea?

SLOW HARVEST: Gathering Your Seasons in a Town that Forgets Stillness

```html
<!DOCTYPE html>
<html lang="en">
<head>
<meta charset="utf-8">
<title>SLOW HARVEST – Book Cover Wrap</title>
<link rel="stylesheet" href="https://fonts.googleapis.com/css2?family=Oswald:wght@500;600;700&family=Roboto:wght@400;700&family=Rubik+Dirt&display=swap">
<style>
  :root {
    --stage: #e4e4e4;
    --cover-dark: #1c1d21;
    --spine-dark: #202227;
    --accent-blue: #27a6e1;
    --text-light: #ffffff;
    --text-soft: #e6e6e6;
    --art-deep: #141c22;
    --art-mid: #3d6f82;
    --art-glow: #9fd0dd;
  }
  * { box-sizing: border-box; margin: 0; padding: 0; }
  html, body { width: 1200px; height: 849px; overflow: hidden; }
  body {
    background: var(--stage);
    font-family: "Roboto", Arial, sans-serif;
    position: relative;
  }
  .book-wrap {
    position: absolute;
    left: 197px; top: 126px;
    width: 807px; height: 594px;
    display: flex;
    box-shadow: 0 4px 14px rgba(0,0,0,.25);
  }

  /* Back cover */
  .back-cover {
    position: relative;
    width: 382px; height: 100%;
    background: var(--cover-dark);
    color: var(--text-light);
    padding: 24px 18px 0;
    text-align: center;
  }
  .back-headline {
    font-family: "Oswald", "Arial Narrow", sans-serif;
    font-weight: 600;
    text-transform: uppercase;
    line-height: 1.25;
  }
  .back-headline .line-white { font-size: 13px; display: block; }
  .back-headline .line-blue { font-size: 16px; color: var(--accent-blue); display: block; }
  .back-body {
    margin-top: 14px;
    font-size: 9.3px;
    line-height: 1.32;
    color: var(--text-soft);
  }
  .back-body p { margin-bottom: 11px; }
  .back-body .tagline { color: var(--accent-blue); }
  .author-bio {
    position: absolute;
    left: 18px; top: 419px;
    width: 250px;
    text-align: left;
    font-size: 10.6px;
    line-height: 1.35;
    color: var(--text-soft);
  }
  .author-bio strong { color: var(--text-light); }
  .author-photo {
    position: absolute;
    left: 288px; top: 419px;
    width: 79px; height: 109px;
    background: linear-gradient(160deg, #d8d4cc 0%, #a9a39a 55%, #2a2a2e 100%);
  }
  .publisher-mark {
    position: absolute;
    left: 22px; top: 556px;
    display: flex; align-items: center; gap: 5px;
    font-size: 7px; font-weight: 700;
    color: var(--accent-blue);
    letter-spacing: .5px;
  }
  .publisher-mark .dot {
    width: 8px; height: 8px; border-radius: 50%;
    background: var(--accent-blue);
  }
  .price {
    position: absolute;
    left: 146px; top: 557px;
    font-size: 6.5px; line-height: 1.4;
    color: var(--text-soft);
    text-align: left;
  }

  /* Spine */
  .spine {
    position: relative;
    width: 49px; height: 100%;
    background: var(--spine-dark);
  }
  .spine-text {
    position: absolute;
    left: 50%; top: 24px;
    transform: translateX(-50%);
    writing-mode: vertical-rl;
    white-space: nowrap;
    display: flex; align-items: center; gap: 30px;
  }
  .spine-title {
    font-family: "Oswald", sans-serif;
    font-weight: 700;
    font-size: 28px;
    color: var(--text-light);
    letter-spacing: 1px;
  }
  .spine-title .cracked { font-family: "Rubik Dirt", "Oswald", sans-serif; font-weight: 400; }
  .spine-author {
    font-family: "Oswald", sans-serif;
    font-weight: 500;
    font-size: 15px;
    color: var(--accent-blue);
    letter-spacing: .5px;
  }
  .spine-mark {
    position: absolute;
    left: 50%; bottom: 28px;
    width: 8px; height: 8px; margin-left: -4px;
    border-radius: 50%;
    background: var(--accent-blue);
  }

  /* Front cover */
  .front-cover {
    position: relative;
    width: 376px; height: 100%;
    background: var(--art-deep);
    overflow: hidden;
    text-align: center;
  }
  .front-art {
    position: absolute; inset: 0;
    background:
      radial-gradient(ellipse 42% 46% at 50% 44%, var(--art-glow) 0%, var(--art-mid) 38%, rgba(30,50,60,.6) 70%, transparent 100%),
      linear-gradient(180deg, #1a242b 0%, #22343d 50%, #161c21 100%);
  }
  .front-subtitle {
    position: relative;
    margin-top: 27px;
    font-family: "Oswald", sans-serif;
    font-weight: 600;
    text-transform: uppercase;
    line-height: 1.15;
  }
  .front-subtitle .sub-blue { display: block; color: var(--accent-blue); font-size: 25px; }
  .front-subtitle .sub-white { display: block; color: var(--text-light); font-size: 16.5px; }
  .front-title {
    position: absolute;
    left: 0; right: 0; top: 476px;
    font-family: "Oswald", sans-serif;
    font-weight: 700;
    font-size: 46px;
    color: var(--text-light);
    letter-spacing: 1px;
  }
  .front-title .cracked { font-family: "Rubik Dirt", "Oswald", sans-serif; font-weight: 400; }
  .front-author {
    position: absolute;
    left: 0; right: 0; top: 548px;
    font-family: "Oswald", sans-serif;
    font-weight: 600;
    font-size: 16px;
    color: var(--accent-blue);
    letter-spacing: .5px;
  }
</style>
</head>
<body>
  <div class="book-wrap">
    <section class="back-cover">
      <h2 class="back-headline">
        <span class="line-white">Women have been told</span>
        <span class="line-blue">We could do and be anything … and we can.</span>
        <span class="line-white">What’s rarely mentioned is the toll on our<br>health, relationships, and overall wellbeing.</span>
      </h2>
      <div class="back-body">
        <p>Are you the woman who holds it all together—crushing deadlines, leading teams, raising a family—while quietly unraveling inside? Yes, you are competent and capable. You’ve simply been carrying more than you were ever meant to for too long.</p>
        <p>Slow Harvest offers a different way forward. Drawn from decades of experience flying commercial aircraft and championing women’s health, retired Captain Delphine Arrowood reveals the missing skill most high-achieving women were never taught: protecting your margins in a world that glorifies overload. This vital buffer not only enables recovery after near-collapse, but also prevents you from reaching the breaking point of exhaustion.</p>
        <p>You will learn about the centuries-old mindset when humans first became cogs in the machine, the science of burnout and brain rewiring, the psychology driving us to push limits, and the cultural systems rigged against women. Discover how to spot the three stages of depletion before they ground you. Through self-assessment tools and actionable practices, the author guides us back home to ourselves by offering a roadmap to rebuild our strength, reconnect with joy and purpose, and redefine success to include true wellbeing.</p>
        <p class="tagline">You don’t need to crash to earn a soft landing. Buckle up! Slow Harvest is your wakeup call to fly lighter and higher than you ever imagined.</p>
      </div>
      <p class="author-bio"><strong>Delphine Arrowood</strong> is a speaker, consultant, and founder of the Skyward Health &amp; Wellbeing Institute. With over 10,000 flight hours, she now empowers women to successfully lead without losing themselves.</p>
      <div class="author-photo" role="img" aria-label="Author portrait photograph"></div>
      <div class="publisher-mark"><span class="dot"></span>EMBERLINE PRESS</div>
      <div class="price">US $19.99<br>CA $23.99</div>
    </section>

    <section class="spine">
      <div class="spine-text">
        <span class="spine-title">SLOW <span class="cracked">HARVEST</span></span>
        <span class="spine-author">CAPT. DELPHINE ARROWOOD</span>
      </div>
      <span class="spine-mark"></span>
    </section>

    <section class="front-cover">
      <div class="front-art" role="img" aria-label="Moody blue-lit photograph of a woman seated with bowed head and hands clasped on her knees"></div>
      <h2 class="front-subtitle">
        <span class="sub-blue">Gathering Your Seasons</span>
        <span class="sub-white">In a Town that Forgets Stillness</span>
      </h2>
      <h1 class="front-title">SLOW <span class="cracked">HARVEST</span></h1>
      <p class="front-author">CAPT. DELPHINE ARROWOOD</p>
    </section>
  </div>
</body>
</html>
```